Business Card Design with new logo

Dorian Pelleway 4172
E 118th St Casey, IL 62420
Cell: 217-555-0193
pellewayrestoration@mailvane.test

Classic Car Restoration Services Buy Sell Trade Consign

Dorian Pelleway 9698
Cell: 217-555-0193

```html
<!DOCTYPE html>
<html lang="en">
<head>
<meta charset="utf-8">
<title>Pelleway Restoration LLC – Business Card Front</title>
<link rel="stylesheet" href="https://fonts.googleapis.com/css2?family=Montserrat:ital,wght@0,700;1,500&display=swap">
<style>
  :root {
    --card-navy: #202a35;
    --card-navy-light: #293a4a;
    --brand-red: #c93b37;
    --text-white: #ffffff;
  }
  * { margin: 0; padding: 0; box-sizing: border-box; }
  html, body {
    width: 1200px;
    height: 720px;
    overflow: hidden;
    background: var(--card-navy);
  }
  .card-front {
    position: relative;
    width: 1200px;
    height: 720px;
    background: var(--card-navy);
    overflow: hidden;
    font-family: "Montserrat", Arial, sans-serif;
  }
  .brand-block {
    position: absolute;
    left: 0;
    top: 244px;
    width: 1200px;
    display: flex;
    flex-direction: column;
    align-items: center;
  }
  .brand-dot {
    width: 112px;
    height: 112px;
    border-radius: 50%;
    background: var(--brand-red);
    margin-bottom: 34px;
  }
  .brand-name {
    color: var(--text-white);
    font-weight: 700;
    font-style: normal;
    text-align: center;
    line-height: 1;
  }
  .brand-name-main {
    display: block;
    font-size: 64px;
    letter-spacing: 0.04em;
  }
  .brand-name-sub {
    display: block;
    margin-top: 14px;
    font-size: 22px;
    letter-spacing: 0.62em;
    padding-left: 0.62em;
  }
  .services-tagline {
    position: absolute;
    left: 0;
    top: 560px;
    width: 1200px;
    text-align: center;
    color: var(--brand-red);
    font-size: 26px;
    font-weight: 500;
    font-style: italic;
    letter-spacing: 0.01em;
  }
</style>
</head>
<body>
  <main class="card-front">
    <div class="brand-block">
      <div class="brand-dot" aria-hidden="true"></div>
      <p class="brand-name">
        <span class="brand-name-main">PELLEWAY</span>
        <span class="brand-name-sub">RESTORATION LLC</span>
      </p>
    </div>
    <p class="services-tagline">Classic Car Restoration Services • Buy • Sell • Trade • Consign</p>
  </main>
</body>
</html>
```